Diesel Fitting/Mechanical Company Needs a new Business Card

We would like a new business card that showcases our logo and business information.

Industry/Entity Type

Business

Contact Information for Business Card

314 Wendale Street
PO Box 7581 BRAMLEY VALE QLD 4871
Phone: 49312787 Fax: 49312688 Mobile: 0438915276 ABN: 63 519 087 342

Requirements
Must have
• The following email addresses:
• admin@tkservicing.com.au , sales@tkservicing.com.au , accounts@tkservicing.com.au , parts@tkservicing.com.au , office@tkservicing.com.au
• Also need to have the website: www.tkservicing.com.au

```html
<!DOCTYPE html>
<html lang="en">
<head>
<meta charset="utf-8">
<title>TK Servicing – Business Card</title>
<link rel="stylesheet" href="https://fonts.googleapis.com/css2?family=Questrial&display=swap">
<style>
  :root{
    --backdrop:#939497;
    --card:#ffffff;
    --ink:#1d1d1d;
    --orange:#e8862e;
    --red:#dc3a3f;
    --band:#0f0f0f;
    --ghost:#f2f2f2;
    --icon:#e8862e;
  }
  *{box-sizing:border-box;margin:0;padding:0}
  html,body{width:1200px;height:1200px;overflow:hidden}
  body{background:var(--backdrop);font-family:"Questrial",Arial,sans-serif;color:var(--ink);position:relative}
  .card{position:absolute;left:190px;width:820px;height:500px;background:var(--card);border-radius:40px;overflow:hidden}
  .card--front{top:60px}
  .card--back{top:640px}

  /* front */
  .front-ghost{position:absolute;left:0;right:0;top:150px;text-align:center;font-size:130px;color:var(--ghost);letter-spacing:2px;line-height:1;white-space:nowrap}
  .front-mark{position:absolute;right:50px;bottom:60px;display:flex;align-items:center;gap:12px;font-size:34px;color:var(--orange)}
  .mark-dot{width:22px;height:22px;border-radius:50%;background:var(--red);flex:none}

  /* back */
  .back-mark{position:absolute;left:60px;top:60px;display:flex;align-items:center;gap:16px;font-size:50px;color:var(--orange);line-height:1;white-space:nowrap}
  .back-mark .mark-dot{width:30px;height:30px}
  .abn{position:absolute;right:60px;top:58px;font-size:29px;color:var(--red);letter-spacing:.5px;white-space:nowrap}
  .emails{position:absolute;left:440px;top:118px;list-style:none}
  .emails li,.contacts li{display:flex;align-items:center;gap:12px;font-size:21px;line-height:31px;white-space:nowrap}
  .contacts{position:absolute;left:60px;top:215px;list-style:none}
  .contacts li{line-height:38px}
  .icon{width:18px;height:18px;flex:none;stroke:var(--icon);fill:none;stroke-width:1.6}
  .address-band{position:absolute;left:0;right:0;bottom:0;height:110px;background:var(--band);color:var(--orange);text-align:center;font-size:22px;line-height:30px;padding-top:24px;white-space:nowrap}
</style>
</head>
<body>

<section class="card card--front" aria-label="Card front">
  <div class="front-ghost" aria-hidden="true">TK Servicing</div>
  <div class="front-mark"><span class="mark-dot"></span>TK Servicing</div>
</section>

<section class="card card--back" aria-label="Card back">
  <div class="back-mark"><span class="mark-dot"></span>TK Servicing</div>
  <div class="abn">ABN: 63 519 087 342</div>

  <ul class="emails">
    <li><svg class="icon" viewBox="0 0 18 18"><rect x="1.5" y="4" width="15" height="10"/><path d="M1.5 4l7.5 6 7.5-6M1.5 14l5.5-5M16.5 14l-5.5-5"/></svg>admin@tkservicing.com.au</li>
    <li><svg class="icon" viewBox="0 0 18 18"><rect x="1.5" y="4" width="15" height="10"/><path d="M1.5 4l7.5 6 7.5-6M1.5 14l5.5-5M16.5 14l-5.5-5"/></svg>sales@tkservicing.com.au</li>
    <li><svg class="icon" viewBox="0 0 18 18"><rect x="1.5" y="4" width="15" height="10"/><path d="M1.5 4l7.5 6 7.5-6M1.5 14l5.5-5M16.5 14l-5.5-5"/></svg>accounts@tkservicing.com.au</li>
    <li><svg class="icon" viewBox="0 0 18 18"><rect x="1.5" y="4" width="15" height="10"/><path d="M1.5 4l7.5 6 7.5-6M1.5 14l5.5-5M16.5 14l-5.5-5"/></svg>parts@tkservicing.com.au</li>
    <li><svg class="icon" viewBox="0 0 18 18"><rect x="1.5" y="4" width="15" height="10"/><path d="M1.5 4l7.5 6 7.5-6M1.5 14l5.5-5M16.5 14l-5.5-5"/></svg>office@tkservicing.com.au</li>
  </ul>

  <ul class="contacts">
    <li><svg class="icon" viewBox="0 0 18 18"><path d="M4 2l3 3-1.5 2a9 9 0 005.5 5.5L13 11l3 3-2 2C8 16 2 10 2 4z"/></svg>49312787</li>
    <li><svg class="icon" viewBox="0 0 18 18"><rect x="5" y="1.5" width="8" height="15" rx="1.5"/><path d="M8 14h2"/></svg>0438915276</li>
    <li><svg class="icon" viewBox="0 0 18 18"><rect x="2" y="7" width="14" height="8"/><path d="M5 7V2h8v5M5 12h8"/></svg>49312688</li>
    <li><svg class="icon" viewBox="0 0 18 18"><circle cx="9" cy="9" r="7"/><path d="M2 9h14M9 2c-3 4-3 10 0 14M9 2c3 4 3 10 0 14"/></svg>www.tkservicing.com.au</li>
  </ul>

  <div class="address-band">
    314 Wendale Street<br>
    PO Box 7581 BRAMLEY VALE QLD 4871
  </div>
</section>

</body>
</html>
```